TAVRO Capital Group LLC a High Risk Big Rewards company for Rich Young Entrepreneurs

We would like a very modern, powerful in the eyes of our customers, modern, minimalist feel, financial gain. this business card is for young Rich entrepreneurs who want to invest money into High Risk, Big Rewards Businesses. The card Should sell the business!! let your creativity go Wild! I pick most of the designers for this project because of your BOLD Designs, I would like this card to be Bold, Modern, Minimalist, use as many effects in your graphic Artist Mind, Do not let the Financial sound of this business to make you think Conservative that's the last thing we are! if you have a lot of money and you want to play a risky market call US
Updates

Project Deadline Extended
Reason: have not received, enough designs to choose 1st and second place, sure I have received over 100 designs but it seems most designers are submitting every card they have ever made before and calling it mine, please we are looking for fresh ideas please!

Target Market(s)

Private Risky Investors

Industry/Entity Type

Financial

Contact Information for Business Card

powerful in the eyes of our customers,modern, minimalist feel

Font styles to use
Other font styles liked:
• Modern feeling fonts

Requirements
Must have
• The Company Name is TAVRO Capital Group LLC and it must be on the CARD
• My Name, title, Cell , email
• Delvin Ashcroft G.E.D.
• Managing Member
• 555.038.6195
• delvin@tavrocapitalgroup.example
Nice to have
• try a black thick plastic card with round corners with Delvin Ashcroft GED (make sure GED is smaller than name) just on one side of the card, and my phone number with out the icons and email on the other side, this card should look like a exclusive credit card or exclusive VIP card, something you would never loose

```html
<!DOCTYPE html>
<html lang="en">
<head>
<meta charset="utf-8">
<title>TAVRO Capital Group LLC – Business Card</title>
<link href="https://fonts.googleapis.com/css2?family=Roboto:wght@400&family=Archivo:wght@800&display=swap" rel="stylesheet">
<style>
  :root {
    --backdrop: #8e8f90;
    --card-black: #232323;
    --card-white: #ecedee;
    --ink: #161616;
    --gold: #c6a43a;
    --gold-light: #dcc25e;
    --gold-dark: #a8852a;
  }
  * { margin: 0; padding: 0; box-sizing: border-box; }
  html, body {
    width: 1200px;
    height: 900px;
    overflow: hidden;
    background: var(--backdrop);
  }
  .canvas {
    position: relative;
    width: 1200px;
    height: 900px;
  }
  .card {
    position: absolute;
    left: 321px;
    width: 522px;
    height: 289px;
  }
  .card--front { top: 120px; background: var(--card-black); }
  .card--back  { top: 472px; background: var(--card-white); }

  .foil {
    position: absolute;
    background: linear-gradient(100deg, var(--gold-dark) 0%, var(--gold) 30%, var(--gold-light) 55%, var(--gold) 75%, var(--gold-dark) 100%);
  }
  .foil--tab { left: 17px; top: 219px; width: 14px; height: 38px; }
  .foil--bar { left: 342px; top: 219px; width: 163px; height: 38px; }

  .holder-name {
    position: absolute;
    left: 51px;
    top: 215px;
    font-family: "Roboto", Arial, sans-serif;
    font-weight: 400;
    font-size: 20px;
    letter-spacing: 0.3px;
    color: var(--gold);
    text-transform: uppercase;
    white-space: nowrap;
  }
  .holder-name .credential { font-size: 20px; }
  .holder-title {
    position: absolute;
    left: 51px;
    top: 243px;
    font-family: "Roboto", Arial, sans-serif;
    font-size: 13px;
    letter-spacing: 0.4px;
    color: var(--gold);
    text-transform: uppercase;
  }

  .company-name {
    position: absolute;
    left: 51px;
    top: 47px;
    font-family: "Archivo", Arial, sans-serif;
    font-weight: 800;
    font-size: 16px;
    letter-spacing: 0.4px;
    color: var(--ink);
    text-transform: uppercase;
  }
  .contact {
    position: absolute;
    left: 51px;
    top: 219px;
    font-family: "Roboto", Arial, sans-serif;
    font-size: 15.5px;
    line-height: 21px;
    color: var(--ink);
    list-style: none;
  }
  .contact__label { display: inline-block; width: 22px; }
</style>
</head>
<body>
<main class="canvas">
  <section class="card card--front">
    <div class="foil foil--tab"></div>
    <h1 class="holder-name">Delvin Ashcroft <span class="credential">G.E.D.</span></h1>
    <p class="holder-title">Managing Member</p>
    <div class="foil foil--bar"></div>
  </section>

  <section class="card card--back">
    <h2 class="company-name">TAVRO Capital Group LLC</h2>
    <div class="foil foil--tab"></div>
    <ul class="contact">
      <li><span class="contact__label">T</span>555.038.6195</li>
      <li><span class="contact__label">E</span>delvin@tavrocapitalgroup.example</li>
    </ul>
    <div class="foil foil--bar"></div>
  </section>
</main>
</body>
</html>
```